Web Design Project

We are looking for a new site design for the VELTO Canada. The current site can be found at
http://www.veltocanada-example.org/
The URL is provided for reference. We want a completely different look and layout which is shown in the specifications document.
As part of the design, we want a home page, and inside page.
The design you provide will be implemented in Joomla. The design winner will only need to provide the PSD. We anticipate creating the template coding in-house.
However, if you have experience creating Joomla templates, please let us know as we may ask you to bid separately to do that phase of the project.
We've provided a specifications document which includes wireframes of the home page, and inside page. We've also included a logo file.
For the header at the top, as indicated in the specs document, we want to keep the same overall treatment to every page. We want a graphic treatment with the logo for the header area. In this manner, the design will be flexiable and can be used for future years.
For the home page, we've indicated that we'd like to have a slider implemented within the design.
The wireframe is provided to illustrate the placement of content and menu items. The exact dimensions of each component can be revised as you see fit. We are also flexiable if you feel we have missed items.

```html
<!DOCTYPE html>
<html lang="en">
<head>
<meta charset="utf-8">
<title>VELTO Canada – Home</title>
<link href="https://fonts.googleapis.com/css2?family=Abel&family=PT+Sans:wght@400;700&display=swap" rel="stylesheet">
<style>
:root{
  --red:#d8262c;
  --red-dark:#b81c22;
  --navy:#0e2a78;
  --navy-deep:#061a55;
  --nav-top:#5b7fd0;
  --nav-bottom:#2f55b0;
  --hero-bg:#140a06;
  --hero-accent:#8fa3ee;
  --link-blue:#2a4aa0;
  --text:#333;
  --muted:#555;
  --border:#c9c9c9;
  --head-top:#ffffff;
  --head-bottom:#d9d9d9;
}
*{margin:0;padding:0;box-sizing:border-box}
html,body{width:1200px;height:900px;overflow:hidden;background:#fff}
body{position:relative;font-family:"PT Sans",Arial,sans-serif;color:var(--text)}
a{text-decoration:none;color:inherit}
.abs{position:absolute}

/* utility bar */
.utility{left:861px;top:0;width:311px;height:26px;background:var(--red);border-radius:0 0 10px 10px;
  display:flex;align-items:center;justify-content:center;font-size:15px;color:#fff;gap:7px}
.utility .current{color:#111}

/* header */
.masthead{left:0;top:45px;width:1200px;height:87px;background:linear-gradient(90deg,var(--navy-deep),var(--navy) 50%,#15358c 100%)}
.masthead-art{position:absolute;left:105px;top:0;width:1095px;height:87px;
  background:linear-gradient(90deg,#12307f 0%,#2a4fb4 35%,#183a98 70%,#102c7c 100%)}
.brand{position:absolute;left:0;top:0;width:105px;height:87px;background:#fff;
  display:flex;align-items:center;justify-content:center;gap:4px;
  font-family:"PT Sans",sans-serif;font-weight:700;font-size:19px;color:var(--navy)}
.brand i{display:block;width:9px;height:9px;background:var(--red)}

/* main navigation */
.main-nav{left:0;top:142px;width:1200px;height:41px;background:linear-gradient(var(--nav-top),var(--nav-bottom));
  font-family:"Abel",sans-serif;font-size:20px;color:#fff}
.main-nav a{position:absolute;top:9px}

/* hero slider */
.hero{left:0;top:195px;width:1200px;height:275px;background:var(--hero-bg)}
.hero-photo{position:absolute;left:70px;top:0;width:592px;height:275px;
  background:radial-gradient(ellipse 240px 120px at 330px 165px,#e0892a 0%,#8a3d10 45%,rgba(20,10,6,0) 100%),
  radial-gradient(ellipse 90px 60px at 140px 150px,#c66a1e 0%,rgba(20,10,6,0) 100%),#231008}
.hero .kicker{position:absolute;left:701px;top:20px;font-size:23px;color:var(--hero-accent);letter-spacing:.3px}
.hero .dots{position:absolute;left:961px;top:23px;display:flex;gap:6px}
.hero .dots span{width:12px;height:12px;border-radius:50%;background:#c4d0f5}
.hero .dots span:first-child{background:#6d87d8}
.hero h2{position:absolute;left:701px;top:63px;font-weight:400;font-size:19px;color:#fff}
.hero .date{position:absolute;left:701px;top:103px;font-size:16px;color:var(--hero-accent)}
.hero p{position:absolute;left:699px;top:136px;width:470px;font-size:16.5px;line-height:29px;color:#fff}
.btn-read{position:absolute;left:697px;top:209px;width:121px;height:34px;border-radius:17px;
  background:linear-gradient(#6d8ee0,#2e4fae);color:#fff;font-size:16px;display:flex;align-items:center;justify-content:center}

/* side panels */
.panel{border:1px solid var(--border);border-radius:5px;background:#fff;overflow:hidden}
.panel-head{height:29px;background:linear-gradient(var(--head-top),var(--head-bottom));border-bottom:1px solid var(--border);
  font-size:16.5px;color:#222;padding:4px 0 0 10px}
.sponsors{left:8px;top:483px;width:283px;height:104px}
.sponsor-row{display:flex;gap:18px;padding:10px 0 0 16px}
.badge{display:block;height:24px;border-radius:3px}
.become{position:absolute;left:64px;top:75px;width:151px;height:21px;background:var(--red-dark);color:#fff;font-size:14px;
  display:flex;align-items:center;justify-content:center;border:1px solid #e46}
.login{left:8px;top:606px;width:283px;height:111px}
.login label{position:absolute;left:18px;font-size:13px;color:#333}
.login .field{position:absolute;left:92px;width:171px;height:17px;border:1px solid #bbb;border-radius:2px}
.btn-login{position:absolute;left:18px;top:85px;width:62px;height:19px;border-radius:10px;
  background:linear-gradient(#4d6dc8,#233f98);color:#fff;font-size:13px;display:flex;align-items:center;justify-content:center}
.connect{left:8px;top:735px;width:283px;height:111px}
.social{position:absolute;top:47px;width:35px;height:35px;border-radius:4px}

/* welcome + news */
.welcome{left:333px;top:484px;width:859px;height:188px;border:1px solid var(--border);border-radius:5px;background:#fff}
.welcome h1{position:absolute;left:10px;top:14px;font-size:16.5px;font-weight:700;color:#555}
.welcome p{position:absolute;left:15px;top:37px;width:528px;font-size:14.3px;line-height:29.3px;color:#333}
.welcome .more{position:absolute;left:15px;top:155px;font-size:14.5px;color:var(--red);font-weight:700}
.news{left:895px;top:493px;width:283px;height:168px}
.news h3{position:absolute;left:11px;top:37px;font-weight:400;font-size:17px;color:var(--link-blue)}
.news .date{position:absolute;left:11px;top:61px;font-size:14px;color:var(--red)}
.news p{position:absolute;left:11px;top:80px;width:258px;font-size:13px;line-height:21px;color:#222;hyphens:manual}
.news p a{color:var(--red);font-size:14px}
.news .more{position:absolute;right:14px;top:134px;font-size:15px;color:var(--red);font-weight:700}

/* regions */
.regions{left:333px;top:680px;width:859px;height:165px}
.regions .cols{display:flex;height:134px}
.region{position:relative;border-right:1px solid var(--border);padding:11px 0 0 0}
.region:last-child{border-right:none}
.region h4{font-weight:400;font-size:17px;color:var(--red);margin-bottom:6px}
.region ul{list-style:none}
.region li{font-size:15px;color:var(--link-blue);line-height:23.5px;padding-left:18px;position:relative}
.region li::before{content:"";position:absolute;left:2px;top:8px;border-left:8px solid var(--link-blue);border-top:4px solid transparent;border-bottom:4px solid transparent}

/* footer */
.footer{left:0;top:855px;width:1200px;height:45px;background:linear-gradient(var(--red),var(--red-dark));color:#fff;font-size:12.5px;text-align:center}
.footer .row1{position:absolute;left:0;right:0;top:6px;padding-left:30px}
.footer .row2{position:absolute;left:0;right:0;top:25px}
.footer .sep{margin:0 6px}
</style>
</head>
<body>

<nav class="utility abs"><a class="current" href="#">Home</a><span>|</span><a href="#">Contact us</a><span>|</span><a href="#">VELTO International</a></nav>

<header class="masthead abs">
  <div class="masthead-art" role="img" aria-label="Decorative blue header graphic"></div>
  <div class="brand"><i></i>VELTO</div>
</header>

<nav class="main-nav abs">
  <a href="#" style="left:9px">About</a>
  <a href="#" style="left:103px">Board</a>
  <a href="#" style="left:185px">Chapters</a>
  <a href="#" style="left:298px">Member Space</a>
  <a href="#" style="left:459px">Resources &amp; knowledge</a>
  <a href="#" style="left:687px">Sponsorship</a>
  <a href="#" style="left:830px">Exhibit</a>
</nav>

<section class="hero abs">
  <div class="hero-photo" role="img" aria-label="Night photo of a glowing industrial drilling site with workers"></div>
  <div class="kicker">ANNOUNCEMENTS</div>
  <div class="dots"><span></span><span></span><span></span><span></span></div>
  <h2>UPCOMING CONFERENCE</h2>
  <div class="date">Jan &nbsp;1, 2012</div>
  <p>Sed ut perspiciatis unde omnis iste natus error sit voluptatem accusantium doloremque laudantium.</p>
  <a class="btn-read" href="#">READ MORE</a>
</section>

<aside class="panel sponsors abs">
  <div class="panel-head">SPONSORS</div>
  <div class="sponsor-row">
    <span class="badge" style="width:72px;background:#222" role="img" aria-label="Sponsor badge"></span>
    <span class="badge" style="width:36px;background:#c8262c" role="img" aria-label="Sponsor badge"></span>
    <span class="badge" style="width:44px;background:#1a7a3a" role="img" aria-label="Sponsor badge"></span>
    <span class="badge" style="width:24px;border-radius:50%;background:#8cc63f" role="img" aria-label="Sponsor badge"></span>
  </div>
  <a class="become" href="#">Become a Sponsor</a>
</aside>

<aside class="panel login abs">
  <div class="panel-head">MEMBER LOGIN</div>
  <label style="top:37px">Username</label><span class="field" style="top:37px"></span>
  <label style="top:64px">Password</label><span class="field" style="top:64px"></span>
  <a class="btn-login" href="#">Login</a>
</aside>

<aside class="panel connect abs">
  <div class="panel-head">STAY CONNECTED</div>
  <span class="social" style="left:61px;background:#2aa3d8" role="img" aria-label="Social network link"></span>
  <span class="social" style="left:111px;background:#1c7bb5" role="img" aria-label="Social network link"></span>
  <span class="social" style="left:162px;background:#3a5a9e" role="img" aria-label="Social network link"></span>
</aside>

<section class="welcome abs">
  <h1>Welcome to VELTO International :</h1>
  <p>Lorem Ipsum is simply dummy text of the printing and typesetting industry. Lorem<br>Ipsum has been the industry's standard dummy text ever since the 1500s, when an<br>unknown printer took a galley of type and scrambled it to make a type specimen<br>book.</p>
  <a class="more" href="#">Read More</a>
</section>

<section class="panel news abs">
  <div class="panel-head">NEWS AND EVENTS</div>
  <h3>Membership &nbsp;participation.</h3>
  <div class="date">Jan &nbsp;1, 2012</div>
  <p>Do you need to convince your employer of<br>the value that your membership and partici-<br>pation. &nbsp;<a href="#">Click here</a></p>
  <a class="more" href="#">READ MORE &#187;</a>
</section>

<section class="panel regions abs">
  <div class="panel-head">REGIONS :</div>
  <div class="cols">
    <div class="region" style="width:200px;padding-left:32px"><h4>Mountain Pacific</h4><ul><li>Vancouver Island</li><li>Vancouver</li><li>Calgary</li></ul></div>
    <div class="region" style="width:199px;padding-left:54px"><h4>Western</h4><ul><li>Edmonton</li><li>Saskatchewan</li><li>Winnipeg</li></ul></div>
    <div class="region" style="width:231px;padding-left:28px"><h4>Central</h4><ul><li>National Capital-Ottawa</li><li>Southwestern Ontario</li><li>Montreal</li><li>Toronto</li></ul></div>
    <div class="region" style="width:227px;padding-left:38px"><h4>Atlantic</h4><ul><li>Nova Scotia</li><li>Terra-Nova,St.John’s</li><li>Prince Edward Island</li><li>Atlantic. St. John’s</li></ul></div>
  </div>
</section>

<footer class="footer abs">
  <div class="row1">Home<span class="sep">|</span>About<span class="sep">|</span>Board<span class="sep">|</span>Chapters<span class="sep">|</span>Member Space<span class="sep">|</span>Resources &amp; knowledge<span class="sep">|</span>Sponsorship<span class="sep">|</span>Exhibit<span class="sep">|</span>Member Login<span class="sep">|</span>Contact Us</div>
  <div class="row2">Privacy Policy &nbsp;&nbsp;Copyright notice</div>
</footer>

</body>
</html>
```